Harborline Ambulatory Flyer

Need to make a flyer similar to the attached Glenmark pdfs for Harborline Ambulatory. The write up is attached or can be found at https://www.velmontcareasc.com/bronx

Requirements
Must have
• What the existing flyer has.

```html
<!DOCTYPE html>
<html lang="en">
<head>
<meta charset="utf-8">
<title>Harborline Ambulatory Surgery Center – Flyer</title>
<link href="https://fonts.googleapis.com/css2?family=Open+Sans:ital,wght@0,400;0,600;0,700;1,600;1,700&display=swap" rel="stylesheet">
<style>
  :root{
    --bg:#e9eaee;
    --navy:#2f5fae;
    --navy-deep:#2a56a3;
    --azure:#1a8fd6;
    --panel-light:#dfe8f5;
    --band-light:#3d73c4;
    --ink:#222833;
    --white:#ffffff;
  }
  *{box-sizing:border-box;margin:0;padding:0}
  html,body{width:1200px;height:1200px;overflow:hidden;background:var(--bg);font-family:"Open Sans",Arial,sans-serif;color:var(--ink)}
  .canvas{position:relative;width:1200px;height:1200px}
  .page{position:absolute;background:var(--white);overflow:hidden}
  .page-front{left:40px;top:100px;width:545px;height:705px}
  .page-back{left:612px;top:322px;width:546px;height:706px}
  .page svg.shapes{position:absolute;left:0;top:0}
  .abs{position:absolute}
  .brand{display:flex;align-items:center;gap:8px;font-weight:700;color:var(--ink);font-size:15px;line-height:1.15}
  .brand-mark{width:12px;height:12px;background:var(--navy);flex:none}
  .brand-rule{position:absolute;height:3px;background:var(--navy)}
  .intro{font-style:italic;font-weight:700;color:var(--navy);text-align:center;font-size:12.5px;line-height:16px}
  .section-bar{background:linear-gradient(90deg,var(--navy),#5b8fd6);color:var(--white);font-weight:700;font-size:11px;line-height:13px;padding:5px 6px}
  .body-copy{font-size:9.6px;line-height:12.4px;text-align:justify}
  .feature{text-align:center;color:var(--navy);font-weight:700;font-size:7.5px;line-height:9.5px}
  .feature-icon{width:48px;height:48px;border-radius:50%;background:var(--azure);margin:0 auto 5px;display:flex;align-items:center;justify-content:center}
  .checklist{list-style:none}
  .checklist li{display:flex;align-items:center;gap:7px}
  .checklist-bold li{color:var(--white);font-weight:700;font-size:13px;line-height:16px}
  .checklist-plain li{color:var(--ink);font-weight:600;font-size:11.2px;line-height:14.3px}
  .footer{position:absolute;left:0;right:0;bottom:0;height:63px;color:var(--white);font-weight:600;font-size:10px;line-height:11.5px}
  .footer-front{background:var(--navy)}
  .footer-back{background:var(--azure)}
  .footer-frame{position:absolute;left:8px;right:8px;top:8px;bottom:8px;border:1.5px solid rgba(255,255,255,.85);border-top:none}
  .contact{position:absolute;display:flex;gap:6px;align-items:flex-start}
  .web-pill{position:absolute;border:1.5px solid var(--white);border-radius:12px;padding:2px 10px 2px 8px;display:flex;gap:5px;align-items:center;font-size:11px;font-weight:700}
  .benefit-title{color:var(--white);font-weight:700;font-size:11px;line-height:14px}
  .benefit-copy{color:var(--white);font-size:9.4px;line-height:12.4px}
  .benefit-icon{position:absolute;width:52px;height:52px;border-radius:50%;background:var(--white);display:flex;align-items:center;justify-content:center}
  .offer-title{color:var(--azure);font-weight:700;font-size:17px;text-decoration:underline;text-underline-offset:3px;text-align:center}
  .location-title{color:var(--azure);font-weight:700;font-size:11px;line-height:13px;text-align:center}
  .location-copy{font-size:9.6px;line-height:12.5px;text-align:center}
  .photo{position:absolute;border-radius:50%;border:4px solid var(--navy)}
</style>
</head>
<body>
<main class="canvas">

  <!-- Front page -->
  <section class="page page-front">
    <svg class="shapes" width="545" height="705" viewBox="0 0 545 705">
      <defs>
        <linearGradient id="lobbyTone" x1="0" y1="0" x2="1" y2="1">
          <stop offset="0" stop-color="#b8c6dc"/><stop offset=".5" stop-color="#cbb79c"/><stop offset="1" stop-color="#dfe6ef"/>
        </linearGradient>
        <linearGradient id="staffTone" x1="0" y1="0" x2="0" y2="1">
          <stop offset="0" stop-color="#dbe6f3"/><stop offset="1" stop-color="#8fb1d8"/>
        </linearGradient>
      </defs>
      <g role="img" aria-label="Photo of a bright clinic reception lobby">
        <rect x="0" y="0" width="545" height="310" fill="url(#lobbyTone)"/>
      </g>
      <path d="M0 0 H320 C250 40 120 95 0 118 Z" fill="var(--white)"/>
      <path d="M320 0 C250 40 120 95 0 118" fill="none" stroke="var(--navy)" stroke-width="5"/>
      <path d="M0 300 C120 290 220 282 300 270 L302 705 H0 Z" fill="var(--white)"/>
      <rect x="302" y="280" width="203" height="160" fill="var(--panel-light)"/>
      <path d="M300 272 C380 258 460 262 545 250 V705 H505 V280 Z" fill="var(--white)"/>
      <rect x="302" y="285" width="203" height="155" fill="var(--panel-light)"/>
      <rect x="302" y="437" width="203" height="180" fill="var(--navy)"/>
      <rect x="302" y="615" width="203" height="10" fill="var(--azure)"/>
      <rect x="8" y="8" width="529" height="640" fill="none" stroke="var(--white)" stroke-width="1.5"/>
      <circle cx="400" cy="215" r="108" fill="none" stroke="var(--navy)" stroke-width="5"/>
      <g role="img" aria-label="Photo of smiling medical staff in white coats">
        <circle cx="400" cy="215" r="100" fill="url(#staffTone)"/>
      </g>
      <path d="M300 260 C330 300 380 320 440 318" fill="none" stroke="var(--navy)" stroke-width="6"/>
    </svg>

    <div class="abs brand" style="left:22px;top:26px;width:220px">
      <span class="brand-mark"></span>
      <span>Harborline Ambulatory<br>Surgery Center</span>
    </div>
    <div class="brand-rule" style="left:22px;top:73px;width:215px"></div>

    <p class="abs intro" style="left:22px;top:304px;width:250px">Harborline Ambulatory Surgery Center, is a same day surgical center, conveniently located in the Bronx, licensed by the state of New York and accredited by NCAFA.</p>

    <div class="abs feature" style="left:308px;top:332px;width:60px">
      <div class="feature-icon"><svg width="26" height="26" viewBox="0 0 26 26"><circle cx="13" cy="13" r="10" fill="none" stroke="#fff" stroke-width="2"/><path d="M5 9 L21 17 M5 17 L21 9" stroke="#fff" stroke-width="1.6"/></svg></div>
      MODERN<br>TECHNOLOGY
    </div>
    <div class="abs feature" style="left:374px;top:347px;width:60px">
      <div class="feature-icon"><svg width="28" height="26" viewBox="0 0 28 26"><path d="M14 2 l2 4 4 .5 -3 3 1 4 -4-2 -4 2 1-4 -3-3 4-.5z" fill="#fff"/><circle cx="7" cy="15" r="3" fill="#fff"/><circle cx="14" cy="16" r="3" fill="#fff"/><circle cx="21" cy="15" r="3" fill="#fff"/><path d="M2 25 q5-8 10 0 M9 25 q5-8 10 0 M16 25 q5-8 10 0" fill="#fff"/></svg></div>
      FIRST CLASS<br>STAFF
    </div>
    <div class="abs feature" style="left:437px;top:332px;width:64px">
      <div class="feature-icon"><svg width="22" height="28" viewBox="0 0 22 28"><path d="M11 1 C5 1 1 5 1 11 c0 7 10 16 10 16 s10-9 10-16 C21 5 17 1 11 1z" fill="#fff"/><circle cx="11" cy="11" r="4" fill="var(--azure)"/></svg></div>
      ACCESSIBILITY
    </div>

    <div class="abs section-bar" style="left:20px;top:400px;width:252px">CAPABILITIES OF HARBORLINE AMBULATORY SURGERY CENTER</div>
    <p class="abs body-copy" style="left:24px;top:443px;width:235px">Harborline Ambulatory Surgery Center is a dedicated facility for same day procedures that do not require an overnight hospital stay, without sacrificing the quality of care and safety that a hospital provides. With over 15,000 sq ft of space and four operating rooms, the center offers specialties including orthopedics, pain management, podiatry, ophthalmology, ENT, pediatric ENT, and general surgery. These same day procedures, are performed by Harborline Ambulatory Surgery Center's highly skilled medical professionals that are committed to patient safety and satisfaction, providing the highest caliber of care with warmth and compassion in a personalized environment.</p>

    <ul class="abs checklist checklist-bold" style="left:328px;top:446px">
      <li><svg width="13" height="13" viewBox="0 0 13 13"><rect x="1" y="2" width="10" height="10" fill="none" stroke="#fff" stroke-width="1.4"/><path d="M3 6 l3 3 6-8" fill="none" stroke="#fff" stroke-width="2"/></svg>ORTHOPEDICS</li>
      <li><svg width="13" height="13" viewBox="0 0 13 13"><rect x="1" y="2" width="10" height="10" fill="none" stroke="#fff" stroke-width="1.4"/><path d="M3 6 l3 3 6-8" fill="none" stroke="#fff" stroke-width="2"/></svg>PAIN MANAGEMENT</li>
      <li><svg width="13" height="13" viewBox="0 0 13 13"><rect x="1" y="2" width="10" height="10" fill="none" stroke="#fff" stroke-width="1.4"/><path d="M3 6 l3 3 6-8" fill="none" stroke="#fff" stroke-width="2"/></svg>SPINE</li>
      <li><svg width="13" height="13" viewBox="0 0 13 13"><rect x="1" y="2" width="10" height="10" fill="none" stroke="#fff" stroke-width="1.4"/><path d="M3 6 l3 3 6-8" fill="none" stroke="#fff" stroke-width="2"/></svg>UROLOGY</li>
      <li><svg width="13" height="13" viewBox="0 0 13 13"><rect x="1" y="2" width="10" height="10" fill="none" stroke="#fff" stroke-width="1.4"/><path d="M3 6 l3 3 6-8" fill="none" stroke="#fff" stroke-width="2"/></svg>GASTROENTEROLOGY</li>
      <li><svg width="13" height="13" viewBox="0 0 13 13"><rect x="1" y="2" width="10" height="10" fill="none" stroke="#fff" stroke-width="1.4"/><path d="M3 6 l3 3 6-8" fill="none" stroke="#fff" stroke-width="2"/></svg>GYNECOLOGY</li>
      <li><svg width="13" height="13" viewBox="0 0 13 13"><rect x="1" y="2" width="10" height="10" fill="none" stroke="#fff" stroke-width="1.4"/><path d="M3 6 l3 3 6-8" fill="none" stroke="#fff" stroke-width="2"/></svg>PLASTIC SURGERY</li>
      <li><svg width="13" height="13" viewBox="0 0 13 13"><rect x="1" y="2" width="10" height="10" fill="none" stroke="#fff" stroke-width="1.4"/><path d="M3 6 l3 3 6-8" fill="none" stroke="#fff" stroke-width="2"/></svg>PODIATRY</li>
      <li><svg width="13" height="13" viewBox="0 0 13 13"><rect x="1" y="2" width="10" height="10" fill="none" stroke="#fff" stroke-width="1.4"/><path d="M3 6 l3 3 6-8" fill="none" stroke="#fff" stroke-width="2"/></svg>OPTHALMOLOGY</li>
      <li><svg width="13" height="13" viewBox="0 0 13 13"><rect x="1" y="2" width="10" height="10" fill="none" stroke="#fff" stroke-width="1.4"/><path d="M3 6 l3 3 6-8" fill="none" stroke="#fff" stroke-width="2"/></svg>ENT</li>
    </ul>

    <footer class="footer footer-front">
      <div class="footer-frame"></div>
      <div class="contact" style="left:24px;top:15px">
        <svg width="9" height="12" viewBox="0 0 9 12"><path d="M4.5 0 C2 0 0 2 0 4.5 c0 3 4.5 7.5 4.5 7.5 s4.5-4.5 4.5-7.5 C9 2 7 0 4.5 0z" fill="#fff"/><circle cx="4.5" cy="4.5" r="1.7" fill="var(--navy)"/></svg>
        <span>2840 Larkspur Ave,<br>Bronx, NY 10468</span>
      </div>
      <div class="contact" style="left:145px;top:15px">
        <svg width="10" height="24" viewBox="0 0 10 24"><path d="M2 1 l2 0 1 3 -1.5 1 q1 2 3 3 l1-1.5 3 1 0 2 q-5 1-8.5-6z" fill="#fff"/><rect x="1" y="15" width="8" height="6" fill="none" stroke="#fff" stroke-width="1"/><path d="M1 15 l4 3 4-3" fill="none" stroke="#fff" stroke-width="1"/></svg>
        <span>(718) 555-0142<br>info@velmontcareasc.com</span>
      </div>
      <div class="web-pill" style="left:302px;top:16px">
        <svg width="10" height="10" viewBox="0 0 10 10"><circle cx="5" cy="5" r="4.3" fill="none" stroke="#fff"/><path d="M.7 5 H9.3 M5 .7 C2.5 3 2.5 7 5 9.3 M5 .7 C7.5 3 7.5 7 5 9.3" fill="none" stroke="#fff" stroke-width=".8"/></svg>
        www.velmontcareasc.com/bronx
      </div>
    </footer>
  </section>

  <!-- Back page -->
  <section class="page page-back">
    <svg class="shapes" width="546" height="706" viewBox="0 0 546 706">
      <defs>
        <linearGradient id="mapTone" x1="0" y1="0" x2="1" y2="1"><stop offset="0" stop-color="#eceef1"/><stop offset="1" stop-color="#d3d7dd"/></linearGradient>
        <linearGradient id="roomTone" x1="0" y1="0" x2="1" y2="1"><stop offset="0" stop-color="#e4f0f8"/><stop offset="1" stop-color="#5aa7da"/></linearGradient>
      </defs>
      <path d="M0 0 H262 C330 110 330 520 252 645 H0 Z" fill="var(--navy-deep)"/>
      <path d="M262 0 C330 110 330 520 252 645" fill="none" stroke="#6b9be0" stroke-width="6"/>
      <path d="M275 0 C342 110 342 520 264 645" fill="none" stroke="#c9d9ef" stroke-width="2"/>
      <rect x="72" y="36" width="205" height="66" fill="var(--band-light)"/>
      <rect x="72" y="242" width="225" height="66" fill="var(--band-light)"/>
      <rect x="72" y="493" width="208" height="64" fill="var(--band-light)"/>
      <rect x="8" y="8" width="530" height="640" fill="none" stroke="var(--navy)" stroke-width="1.2" opacity=".5"/>
      <circle cx="355" cy="540" r="63" fill="var(--azure)"/>
      <g role="img" aria-label="Street map of the surrounding Bronx neighborhood with a location marker">
        <circle cx="355" cy="540" r="59" fill="url(#mapTone)"/>
      </g>
      <circle cx="465" cy="540" r="63" fill="var(--azure)"/>
      <g role="img" aria-label="Photo of a modern operating room">
        <circle cx="465" cy="540" r="59" fill="url(#roomTone)"/>
      </g>
    </svg>

    <div class="benefit-icon" style="left:22px;top:40px"><svg width="28" height="28" viewBox="0 0 28 28"><path d="M3 13 h5 v12 H3z M9 13 l5-9 q3 0 2 5 l-1 3 h8 q3 1 1 4 l-2 8 q-1 2-4 2 H9z" fill="none" stroke="var(--navy)" stroke-width="2" stroke-linejoin="round"/></svg></div>
    <div class="benefit-icon" style="left:22px;top:244px"><svg width="30" height="28" viewBox="0 0 30 28"><path d="M15 14 c-3-3-8-6-5-9 2-2 4-1 5 1 1-2 3-3 5-1 3 3-2 6-5 9z" fill="none" stroke="var(--navy)" stroke-width="1.8"/><path d="M2 12 l3 8 6 6 M28 12 l-3 8 -6 6 M8 18 l4 4 M22 18 l-4 4" fill="none" stroke="var(--navy)" stroke-width="1.8"/></svg></div>
    <div class="benefit-icon" style="left:22px;top:497px"><svg width="30" height="30" viewBox="0 0 30 30"><path d="M15 3 l3.5 7.5 8 1 -6 5.5 1.6 8 -7.1-4 -7.1 4 1.6-8 -6-5.5 8-1z" fill="none" stroke="var(--navy)" stroke-width="1.8" stroke-linejoin="round"/></svg></div>

    <h2 class="abs benefit-title" style="left:83px;top:45px;width:190px">BENEFITS OF CHOSING HARBORLINE AMBULATORY SURGERY CENTER</h2>
    <p class="abs benefit-copy" style="left:23px;top:112px;width:245px">More surgeons are choosing same day surgery centers because of the ability to provide high quality care in a state-of-the-art facility, at a more reasonable cost to you, your insurance provider, and your employer. Perhaps most importantly, same day surgery requires less down time, which means you'll spend less time away from your family and your job, and in most instances, you can return to your daily routine the next day.</p>

    <h2 class="abs benefit-title" style="left:85px;top:249px;width:200px">UNPARALLELED<br>CUSTOMER SERVICE FOR<br>SURGEONS AND PATIENTS</h2>
    <p class="abs benefit-copy" style="left:23px;top:314px;width:250px">At Harborline Ambulatory Surgery Center, we offer an extraordinary team of board-certified anesthesiologists, nurses and on-site clinical and administrative staff who ensure that each surgeon and patient is treated with the highest level of customer service.</p>
    <p class="abs benefit-copy" style="left:23px;top:401px;width:250px">Upon entering our elegant waiting room, through the recovery proces, patients experience individualized care and attention in a safe and luxurious environment. Harborline Ambulatory Surgery Center is highly regarded and has received consistently excellent patient satisfaction surveys.</p>

    <h2 class="abs benefit-title" style="left:85px;top:511px;width:190px">IMPECCABLE STANDARDS OFCLINICAL CARE</h2>
    <p class="abs benefit-copy" style="left:23px;top:567px;width:230px">We are proud to have an outstanding reputation among the area's top surgeons who know they can count on us for efficiency, safety and convenience. We are backed by four major hospitals in Brooklyn.</p>

    <div class="abs brand" style="left:305px;top:36px;width:225px">
      <span class="brand-mark"></span>
      <span>Harborline Ambulatory<br>Surgery Center</span>
    </div>
    <div class="brand-rule" style="left:300px;top:83px;width:220px"></div>

    <p class="abs intro" style="left:298px;top:102px;width:240px;font-size:11.3px">Here at Harborline Ambulatory Surgery Center, the patient is our number one priority. To offer your patients the highest caliber care for same-day surgeries, contact Harborline Ambulatory Surgery Center today.</p>

    <h2 class="abs offer-title" style="left:300px;top:214px;width:235px">WE OFFER</h2>
    <ul class="abs checklist checklist-plain" style="left:345px;top:249px">
      <li><svg width="11" height="11" viewBox="0 0 11 11"><rect x=".5" y="1.5" width="9" height="9" fill="none" stroke="var(--azure)"/><path d="M2.5 5 l2.5 3 5-7" fill="none" stroke="var(--azure)" stroke-width="1.8"/></svg>ORTHOPEDICS</li>
      <li><svg width="11" height="11" viewBox="0 0 11 11"><rect x=".5" y="1.5" width="9" height="9" fill="none" stroke="var(--azure)"/><path d="M2.5 5 l2.5 3 5-7" fill="none" stroke="var(--azure)" stroke-width="1.8"/></svg>PAIN MANAGEMENT</li>
      <li><svg width="11" height="11" viewBox="0 0 11 11"><rect x=".5" y="1.5" width="9" height="9" fill="none" stroke="var(--azure)"/><path d="M2.5 5 l2.5 3 5-7" fill="none" stroke="var(--azure)" stroke-width="1.8"/></svg>PODIATRY</li>
      <li><svg width="11" height="11" viewBox="0 0 11 11"><rect x=".5" y="1.5" width="9" height="9" fill="none" stroke="var(--azure)"/><path d="M2.5 5 l2.5 3 5-7" fill="none" stroke="var(--azure)" stroke-width="1.8"/></svg>OPTHALMOLOGY</li>
      <li><svg width="11" height="11" viewBox="0 0 11 11"><rect x=".5" y="1.5" width="9" height="9" fill="none" stroke="var(--azure)"/><path d="M2.5 5 l2.5 3 5-7" fill="none" stroke="var(--azure)" stroke-width="1.8"/></svg>GENERAL SURGERY</li>
      <li><svg width="11" height="11" viewBox="0 0 11 11"><rect x=".5" y="1.5" width="9" height="9" fill="none" stroke="var(--azure)"/><path d="M2.5 5 l2.5 3 5-7" fill="none" stroke="var(--azure)" stroke-width="1.8"/></svg>ADULT &amp; PEDIATRIC ENT</li>
    </ul>

    <h2 class="abs location-title" style="left:300px;top:357px;width:240px">CONVENIENT LOCATION<br>FOR PATIENTS AND SURGEONS</h2>
    <p class="abs location-copy" style="left:330px;top:393px;width:185px">Harborline Ambulatory Surgery Center is conveniently located on Larkspur Avenue in the Bronx, and is easily accessed from Manhattan, Westchester and Long Island with ample parking available on site.</p>

    <footer class="footer footer-back">
      <div class="footer-frame"></div>
      <div class="contact" style="left:34px;top:14px">
        <svg width="9" height="12" viewBox="0 0 9 12"><path d="M4.5 0 C2 0 0 2 0 4.5 c0 3 4.5 7.5 4.5 7.5 s4.5-4.5 4.5-7.5 C9 2 7 0 4.5 0z" fill="#fff"/><circle cx="4.5" cy="4.5" r="1.7" fill="var(--azure)"/></svg>
        <span>2840 Larkspur Ave,<br>Bronx, NY 10468</span>
      </div>
      <div class="contact" style="left:152px;top:14px">
        <svg width="10" height="24" viewBox="0 0 10 24"><path d="M2 1 l2 0 1 3 -1.5 1 q1 2 3 3 l1-1.5 3 1 0 2 q-5 1-8.5-6z" fill="#fff"/><rect x="1" y="15" width="8" height="6" fill="none" stroke="#fff" stroke-width="1"/><path d="M1 15 l4 3 4-3" fill="none" stroke="#fff" stroke-width="1"/></svg>
        <span>(718) 555-0142<br>info@velmontcareasc.com</span>
      </div>
      <div class="web-pill" style="left:308px;top:15px">
        <svg width="10" height="10" viewBox="0 0 10 10"><circle cx="5" cy="5" r="4.3" fill="none" stroke="#fff"/><path d="M.7 5 H9.3 M5 .7 C2.5 3 2.5 7 5 9.3 M5 .7 C7.5 3 7.5 7 5 9.3" fill="none" stroke="#fff" stroke-width=".8"/></svg>
        www.velmontcareasc.com/bronx
      </div>
    </footer>
  </section>

</main>
</body>
</html>
```